WWW.TRESSALO.IT BUSINNES CARD

WE NEED A BUSINESS CARD . I HAVE A COMPANY IN ITALY NR 1 IN HAIR MEDICAL CARE AN HAIR REPLECEMENT . IN CARD I NEED WRITE WEB ADDRESS, MAIL , ADDRESS, TELEPHONE NUMBER , AND NAME
IN THE BACK SIDE I NEED MY DOCTOR LOGO .
MY WEB SITE IS WWW.TRESSALO.IT
Updates

Hai bisogno di giorni extra per la revisione

Target Market(s)

CONSUMER B2C

Industry/Entity Type

Hair And Beauty

Contact Information for Business Card

I WANT A MEDICAL BUSINESS CARD.

Font styles to use
Other font styles liked:
• VERDANA

Colors
33a6d7
3176b5
85abd2
aedbee
eaf1f7
ffffff

Requirements
Must have
• I NEED MY LOGO AND LOGO OF DR TRESSALO

```html
<!DOCTYPE html>
<html lang="it">
<head>
<meta charset="utf-8">
<title>Tressalo – Biglietto da visita</title>
<link href="https://fonts.googleapis.com/css2?family=Roboto:wght@400;500;700&display=swap" rel="stylesheet">
<style>
  :root{
    --backdrop:#2e2e2e;
    --paper:#f3f3f3;
    --navy:#05508f;
    --sky:#29b3e5;
    --brand-blue:#1a74b8;
    --white:#ffffff;
    --art-dark:#8a5a3a;
    --art-light:#c99877;
  }
  *{margin:0;padding:0;box-sizing:border-box}
  html,body{width:1200px;height:960px;overflow:hidden}
  body{background:var(--backdrop);font-family:"Roboto",Verdana,sans-serif;position:relative}
  .card{position:absolute;width:600px;height:342px;overflow:hidden;box-shadow:0 3px 8px rgba(0,0,0,.5)}
  .card-front{left:313px;top:113px;background:var(--paper)}
  .card-back{left:311px;top:472px;background:var(--sky)}
  .brand{position:absolute;left:0;right:0;top:74px;display:flex;justify-content:center;align-items:center;gap:14px}
  .brand-mark{width:44px;height:44px;background:var(--sky)}
  .brand-name{font-size:54px;font-weight:700;color:var(--brand-blue);line-height:1}
  .tagline{position:absolute;left:0;right:0;top:141px;text-align:center;font-size:15px;font-weight:500;letter-spacing:.4px;color:var(--brand-blue)}
  .wave{position:absolute;left:0;top:0}
  .holder-name{position:absolute;left:37px;top:250px;font-size:22px;font-weight:700;color:var(--white)}
  .holder-address{position:absolute;left:39px;top:284px;font-size:15px;line-height:18px;color:var(--white)}
  .contacts{position:absolute;right:36px;top:262px;list-style:none;font-size:15px;line-height:20px;color:var(--white);text-align:right}
  .contacts li{display:flex;justify-content:flex-end;align-items:center;gap:8px}
  .contacts svg{width:14px;height:14px}
  .back-brand{position:absolute;left:112px;top:118px;font-size:40px;font-weight:700;color:var(--white)}
  .locations{position:absolute;left:32px;width:300px;top:227px;list-style:none;text-align:center;font-size:15px;line-height:18px;color:var(--white)}
  .mascot-art{position:absolute;left:454px;top:16px;width:126px;height:308px;border-radius:8px;background:linear-gradient(180deg,var(--art-dark) 0%,var(--art-light) 100%)}
</style>
</head>
<body>
  <section class="card card-front">
    <svg class="wave" width="600" height="342" viewBox="0 0 600 342" aria-hidden="true">
      <path d="M0 212 C150 180 300 255 600 184 L600 342 L0 342 Z" fill="var(--sky)"/>
      <path d="M0 219 C150 186 300 262 600 189 L600 342 L0 342 Z" fill="var(--white)"/>
      <path d="M0 224 C150 192 300 268 600 194 L600 342 L0 342 Z" fill="var(--navy)"/>
    </svg>
    <div class="brand">
      <span class="brand-mark"></span>
      <span class="brand-name">Tressalo</span>
    </div>
    <p class="tagline">CURA E REINTEGRAZIONE DEI CAPELLI</p>
    <h1 class="holder-name">Luca Bernardi</h1>
    <p class="holder-address">Via dei Tigli 112<br>57126 Livorno, Italy</p>
    <ul class="contacts">
      <li>800275019
        <svg viewBox="0 0 24 24"><path fill="var(--white)" d="M6.6 10.8a15.1 15.1 0 0 0 6.6 6.6l2.2-2.2c.3-.3.7-.4 1-.2 1.1.4 2.3.6 3.6.6.6 0 1 .4 1 1V20c0 .6-.4 1-1 1C10.6 21 3 13.4 3 4c0-.6.4-1 1-1h3.5c.6 0 1 .4 1 1 0 1.3.2 2.5.6 3.6.1.3 0 .7-.2 1z"/></svg>
      </li>
      <li>Luca@tressalo.it
        <svg viewBox="0 0 24 24"><rect x="2" y="5" width="20" height="14" rx="1" fill="var(--white)"/><path d="M2.5 6l9.5 7 9.5-7" fill="none" stroke="var(--navy)" stroke-width="1.8"/></svg>
      </li>
      <li>www.tressalo.it
        <svg viewBox="0 0 24 24"><circle cx="12" cy="12" r="10" fill="var(--white)"/><path d="M2 12h20M12 2c3 3 3 17 0 20M12 2c-3 3-3 17 0 20" stroke="var(--navy)" stroke-width="1.5" fill="none"/></svg>
      </li>
    </ul>
  </section>

  <section class="card card-back">
    <p class="back-brand">Tressalo</p>
    <ul class="locations">
      <li>Via dei Mulini 18, 31100 Treviso, Italy</li>
      <li>Via Cesare 40, 37121 Verona, Italy</li>
      <li>Via del Pino 53, 50136 Florence, Italy</li>
      <li>Via dei Tigli 112, 57126 Livorno, Italy</li>
    </ul>
    <div class="mascot-art" role="img" aria-label="Mascot illustration"></div>
  </section>
</body>
</html>
```